An international wholesale business needs letterhead design

Logo file is attached. Please design a letterhead with the following details:

- Company Name and Logo
- Address
- VAT Registration number
- Phone No
- Website address

```html
<!DOCTYPE html>
<html lang="en">
<head>
<meta charset="utf-8">
<title>Corvell Trading Letterhead</title>
<link href="https://fonts.googleapis.com/css2?family=Montserrat:wght@500;600;700&family=Lato:wght@400;700&family=Dancing+Script:wght@600&display=swap" rel="stylesheet">
<style>
  :root {
    --brand-red: #c1272d;
    --brand-grey: #8a8f96;
    --ink: #2b2b2b;
    --paper: #ffffff;
    --backdrop: #e4e5e7;
  }
  * { margin: 0; padding: 0; box-sizing: border-box; }
  html, body { width: 1200px; height: 960px; overflow: hidden; background: var(--backdrop); }
  .letterhead {
    position: absolute; left: 282px; top: 30px;
    width: 636px; height: 900px;
    background: var(--paper);
    box-shadow: 0 6px 24px rgba(0,0,0,0.12);
    overflow: hidden;
    font-family: "Lato", sans-serif; color: var(--ink);
  }
  .brand { position: absolute; left: 42px; top: 96px; display: flex; align-items: center; gap: 10px; }
  .brand-dot { width: 34px; height: 34px; border-radius: 50%; background: var(--brand-red); }
  .brand-name { font-family: "Montserrat", sans-serif; font-weight: 700; font-size: 30px; letter-spacing: 2px; color: var(--brand-red); }
  .contact { position: absolute; right: 48px; top: 34px; font-family: "Montserrat", sans-serif; font-size: 10.5px; line-height: 15px; color: var(--ink); }
  .contact-title { font-weight: 700; color: var(--brand-red); font-size: 11px; }
  .contact-row { display: flex; align-items: center; gap: 6px; padding-left: 14px; }
  .contact-row svg { width: 9px; height: 9px; fill: var(--brand-red); }
  .contact-address { padding-left: 14px; }
  .rule { position: absolute; left: 95px; right: 50px; top: 172px; height: 1.5px; background: var(--brand-red); }
  .letter { position: absolute; left: 95px; top: 210px; width: 490px; font-size: 10.5px; line-height: 15px; }
  .letter-date { font-family: "Montserrat", sans-serif; font-size: 12px; margin-bottom: 22px; }
  .recipient { font-family: "Montserrat", sans-serif; font-size: 11px; line-height: 14px; margin-bottom: 16px; }
  .recipient-company { margin-top: 14px; }
  .salutation { font-family: "Montserrat", sans-serif; font-weight: 700; font-size: 14px; margin-bottom: 14px; }
  .letter p.body { margin-bottom: 14px; }
  .closing { margin-top: 26px; font-family: "Montserrat", sans-serif; font-size: 11px; }
  .signature { font-family: "Dancing Script", cursive; font-size: 34px; margin-top: 10px; margin-left: 40px; }
  .footer-wave { position: absolute; left: 0; bottom: 0; width: 636px; height: 260px; }
  .vat { position: absolute; right: 40px; bottom: 22px; font-family: "Montserrat", sans-serif; font-size: 11px; color: var(--paper); }
</style>
</head>
<body>
<main class="letterhead">
  <header>
    <div class="brand">
      <span class="brand-dot"></span>
      <span class="brand-name">CORVELL</span>
    </div>
    <address class="contact" style="font-style: normal;">
      <div class="contact-title">CORVELL TRADING</div>
      <div class="contact-address">4100 W Harmon Rd Ste 210<br>Fairview, TX 75069</div>
      <div class="contact-row">
        <svg viewBox="0 0 10 10"><path d="M2 0.5 L3.8 2.6 L2.9 3.8 C3.6 5.2 4.8 6.4 6.2 7.1 L7.4 6.2 L9.5 8 L8.2 9.5 C4.2 9 1 5.8 0.5 1.8 Z"/></svg>
        <span>555-318-4420</span>
      </div>
      <div class="contact-row">
        <svg viewBox="0 0 10 10"><path d="M0 2 H10 V8.5 H0 Z M0.6 2.4 L5 5.8 L9.4 2.4" stroke="#fff" stroke-width="0.8"/></svg>
        <span>hello@corvelltrading.com</span>
      </div>
      <div class="contact-row">
        <svg viewBox="0 0 10 10"><circle cx="5" cy="5" r="4.6"/><path d="M0.5 5 H9.5 M5 0.4 C2.6 3 2.6 7 5 9.6 M5 0.4 C7.4 3 7.4 7 5 9.6" stroke="#fff" stroke-width="0.6" fill="none"/></svg>
        <span>www.corvelltrading.com</span>
      </div>
    </address>
    <div class="rule"></div>
  </header>

  <article class="letter">
    <p class="letter-date">January-03-2020</p>
    <div class="recipient">
      <div>Mr, Owen Pratt</div>
      <div>President</div>
      <div class="recipient-company">Brightway Holdings</div>
      <div>123 Street Name, Suite# 10</div>
      <div>City, State, 120023</div>
    </div>
    <p class="salutation">Dear Mr, Owen</p>
    <p class="body">Lorem ipsum dolor sit amet, consectetur adipisicing elit, sed do eiusmod tempor incididunt ut labore et dolore magna aliqua. Ut enim ad minim veniam, quis nostrud exercitation ullamco laboris nisi ut aliquip ex ea commodo consequat. Duis aute irure dolor in reprehenderit in voluptate velit esse cillum dolore eu fugiat nulla pariatur.</p>
    <p class="body">Lorem ipsum dolor sit amet, consectetur adipisicing elit, sed do eiusmod tempor incididunt ut labore et dolore magna aliqua. Ut enim ad minim veniam, quis nostrud exercitation ullamco laboris nisi ut aliquip ex ea commodo consequat. Duis aute irure dolor in reprehenderit in voluptate velit esse cillum dolore eu fugiat nulla pariatur.</p>
    <p class="body">Lorem ipsum dolor sit amet, consectetur adipisicing elit, sed do eiusmod tempor incididunt ut labore et dolore magna aliqua. Ut enim ad minim veniam, quis nostrud exercitation ullamco laboris nisi ut aliquip ex ea commodo consequat.</p>
    <p class="body">Excepteur sint occaecat cupidatat non proident, sunt in culpa qui officia deserunt mollit anim id est laborum. re et dolore magnam aliquam quaerat voluptatem.</p>
    <p class="closing">Regards</p>
    <p class="signature">Daniel Reyes</p>
  </article>

  <footer>
    <svg class="footer-wave" viewBox="0 0 636 260" preserveAspectRatio="none" aria-hidden="true">
      <path d="M0 258 C150 254 260 238 360 212 C480 180 560 140 600 90 C618 66 630 36 636 10 L636 260 L0 260 Z" fill="var(--brand-grey)"/>
      <path d="M0 262 C150 260 262 246 364 220 C484 190 566 150 606 100 C622 80 632 56 636 36 L636 260 L0 260 Z" fill="var(--brand-red)"/>
    </svg>
    <p class="vat">VAT Registration number: 555 0142</p>
  </footer>
</main>
</body>
</html>
```